Structural Engineering Business Card

Orvik Drafting does residential house plans for clients in Central Florida. Would like simple but elegant business card that is appropriate for a house plan engineering company. Prefer black business card with black/white them but open to other shades of blue. I uploaded a sample card that I came across that looked good but please come up with your own creative designs.

Contact Information for Business Card

Name, Title, Phone, Email, Address, website

```html
<!DOCTYPE html>
<html lang="en">
<head>
<meta charset="utf-8">
<title>Orvik Drafting – Business Card</title>
<link href="https://fonts.googleapis.com/css2?family=Arimo:wght@400;700&display=swap" rel="stylesheet">
<style>
  :root {
    --backdrop: #2b2b2b;
    --card: #1c1c1c;
    --ink: #ffffff;
    --ink-soft: #e8e8e8;
  }
  * { margin: 0; padding: 0; box-sizing: border-box; }
  html, body {
    width: 1200px;
    height: 1059px;
    overflow: hidden;
    background: var(--backdrop);
    font-family: "Arimo", Arial, sans-serif;
    color: var(--ink);
  }
  .card {
    position: absolute;
    left: 256px;
    width: 690px;
    height: 400px;
    background: var(--card);
    border-radius: 16px;
  }
  .card--front { top: 90px; }
  .card--back { top: 560px; }

  .brand {
    position: absolute;
    left: 0;
    right: 0;
    display: flex;
    align-items: center;
    justify-content: center;
    gap: 14px;
    font-weight: 700;
    letter-spacing: 0.02em;
    text-transform: uppercase;
    color: var(--ink);
  }
  .brand__mark {
    background: var(--ink);
    flex: none;
  }
  .card--front .brand { top: 76px; font-size: 40px; }
  .card--front .brand__mark { width: 30px; height: 30px; }
  .card--back .brand { top: 166px; font-size: 56px; gap: 18px; }
  .card--back .brand__mark { width: 42px; height: 42px; }

  .person {
    position: absolute;
    right: 373px;
    top: 224px;
    text-align: right;
  }
  .person__name {
    font-weight: 700;
    font-size: 24px;
    letter-spacing: 0.02em;
    line-height: 1.1;
  }
  .person__title {
    font-size: 17px;
    color: var(--ink-soft);
    margin-top: 2px;
  }
  .divider {
    position: absolute;
    left: 343px;
    top: 215px;
    width: 1px;
    height: 70px;
    background: var(--ink);
  }
  .contact {
    position: absolute;
    left: 367px;
    top: 209px;
    list-style: none;
  }
  .contact__item {
    display: flex;
    align-items: center;
    gap: 6px;
    font-size: 17px;
    height: 29px;
  }
  .contact__icon { width: 13px; height: 13px; fill: var(--ink); flex: none; }
  .address {
    position: absolute;
    left: 0;
    right: 0;
    top: 330px;
    text-align: center;
    font-size: 17px;
    color: var(--ink-soft);
  }
</style>
</head>
<body>
  <section class="card card--front">
    <div class="brand"><span class="brand__mark"></span><span>Orvik Drafting</span></div>

    <div class="person">
      <p class="person__name">DANA WHITLOW</p>
      <p class="person__title">Founder/CEO</p>
    </div>
    <div class="divider"></div>
    <ul class="contact">
      <li class="contact__item">
        <svg class="contact__icon" viewBox="0 0 16 16" aria-hidden="true"><path d="M2 5c0-2 2-3 6-3s6 1 6 3v1h-3V5H5v1H2zM4 7h8l2 6H2z"/></svg>
        555.014.2290
      </li>
      <li class="contact__item">
        <svg class="contact__icon" viewBox="0 0 16 16" aria-hidden="true"><path d="M1 3h14v1L8 9 1 4zM1 6l7 5 7-5v7H1z"/></svg>
        info@orvikdrafting.com
      </li>
      <li class="contact__item">
        <svg class="contact__icon" viewBox="0 0 16 16" aria-hidden="true"><circle cx="8" cy="8" r="6.5" fill="none" stroke="#fff" stroke-width="1.5"/><path d="M5 5h3l1 2-2 2 1 3-3-2zM10 4l2 1v3h-2z"/></svg>
        www.orvikdrafting.com
      </li>
    </ul>
    <p class="address">1270 Harbor Blvd Suite 310 Lakemont, FL 32804</p>
  </section>

  <section class="card card--back">
    <div class="brand"><span class="brand__mark"></span><span>Orvik Drafting</span></div>
  </section>
</body>
</html>
```